Brightmere Business Card Redesign & Logo Update

We need to update our business cards to something more modern and fresh. Brightmere can provide the current color schemes and old design examples, but welcome creativity in helping us with this redesign. PLEASE NOTE that we no longer utilize the "tree" and/or "leaf" imagery in our branding. If able would apprecaite an update on the quality of our "words only" logo in Ai. / PNG formats too.

Target Market(s)

Investors, landowners, corporate partners, contractors

Industry/Entity Type

Environmental Restoration & Conservation

Contact Information for Business Card

Logo, persons name, title, mailing address, phone and email, website url

Font styles to use
Other font styles liked:
• Merriweather

Requirements
Nice to have
• Logo, persons name, title, mailing address, phone and email, website url, but open to ideams
Should not have
• No all back backgrounds

```html
<!DOCTYPE html>
<html lang="en">
<head>
<meta charset="utf-8">
<title>Brightmere Business Card</title>
<link rel="stylesheet" href="https://fonts.googleapis.com/css2?family=Bebas+Neue&family=Montserrat:wght@400;500;700&display=swap">
<style>
  :root {
    --orange: #ec7d25;
    --green: #167c3c;
    --white: #ffffff;
    --ink: #1c1c1c;
    --map-tint: #f5c395;
    --stage: #ebe8e3;
  }
  * { box-sizing: border-box; margin: 0; padding: 0; }
  html, body { width: 901px; height: 1200px; overflow: hidden; }
  body { background: var(--stage); position: relative; font-family: "Montserrat", sans-serif; }

  .card {
    position: absolute;
    left: 87px;
    width: 727px;
    height: 422px;
    border-radius: 22px;
    overflow: hidden;
    box-shadow: 0 6px 14px rgba(0,0,0,0.25);
  }
  .card-front { top: 143px; background: var(--white); }
  .card-back { top: 629px; background: var(--orange); }
  .card-decor { position: absolute; inset: 0; }

  .person-name {
    position: absolute; left: 34px; top: 84px;
    font-weight: 700; font-size: 23px; letter-spacing: 0.2px;
  }
  .person-name .first { color: var(--green); }
  .person-name .last { color: var(--orange); }
  .person-title {
    position: absolute; left: 34px; top: 116px;
    font-size: 16.5px; color: var(--ink);
  }

  .brand-lockup {
    position: absolute; text-align: center; white-space: nowrap;
    font-family: "Bebas Neue", sans-serif;
  }
  .brand-name, .brand-tagline { display: block; line-height: 1; }

  .card-front .brand-lockup { right: 34px; top: 74px; width: 310px; }
  .card-front .brand-name { font-size: 76px; color: var(--green); }
  .card-front .brand-tagline { font-size: 26px; color: var(--ink); margin-top: 2px; }

  .contact-list { position: absolute; left: 34px; top: 261px; list-style: none; }
  .contact-list li {
    display: flex; align-items: center; height: 32px;
    font-size: 19px; color: var(--ink);
  }
  .contact-icon { width: 26px; height: 26px; margin-right: 12px; flex: none; }

  .mailing-address {
    position: absolute; right: 35px; top: 305px;
    font-size: 17.5px; line-height: 27px; text-align: right; color: var(--ink);
    font-style: normal;
  }

  .world-map {
    position: absolute; left: 54px; top: 28px; width: 624px; height: 362px;
    background: radial-gradient(ellipse at center, rgba(245,195,149,0.75) 0%, rgba(245,195,149,0.45) 55%, rgba(245,195,149,0) 75%);
  }
  .card-back .brand-lockup { left: 0; right: 0; top: 130px; }
  .card-back .brand-name { font-size: 124px; color: var(--white); }
  .card-back .brand-tagline { font-size: 36px; color: var(--white); margin-top: 2px; }
</style>
</head>
<body>

<section class="card card-front">
  <svg class="card-decor" viewBox="0 0 727 422" width="727" height="422" aria-hidden="true">
    <polygon fill="var(--orange)" points="0,0 727,0 727,24 260,24 239,46 0,46"/>
    <rect fill="var(--green)" x="252" y="34" width="183" height="9"/>
    <rect fill="var(--orange)" x="441" y="34" width="123" height="9"/>
    <rect fill="var(--green)" x="571" y="34" width="156" height="9"/>
    <polygon fill="var(--orange)" points="486,374 727,374 727,422 0,422 0,396 462,396"/>
    <rect fill="var(--green)" x="0" y="377" width="152" height="9"/>
    <rect fill="var(--orange)" x="158" y="377" width="124" height="9"/>
    <polygon fill="var(--green)" points="287,377 469,377 460,386 287,386"/>
  </svg>

  <div class="person-name"><span class="first">JON</span> <span class="last">HARLOWE</span></div>
  <div class="person-title">Managing Director</div>

  <div class="brand-lockup">
    <span class="brand-name">BRIGHTMERE</span>
    <span class="brand-tagline">Environmental Credit Company</span>
  </div>

  <ul class="contact-list">
    <li>
      <svg class="contact-icon" viewBox="0 0 26 26" aria-hidden="true">
        <circle cx="13" cy="13" r="13" fill="var(--orange)"/>
        <path fill="var(--white)" d="M6 11c0-3 14-3 14 0v1.5h-3.5V11h-7v1.5H6z"/>
        <rect fill="var(--white)" x="8" y="13" width="10" height="6" rx="1"/>
      </svg>
      555-014-2290
    </li>
    <li>
      <svg class="contact-icon" viewBox="0 0 26 26" aria-hidden="true">
        <circle cx="13" cy="13" r="13" fill="var(--orange)"/>
        <rect x="6.5" y="8.5" width="13" height="9" fill="none" stroke="var(--white)" stroke-width="1.6"/>
        <path d="M6.5 8.5 13 14l6.5-5.5" fill="none" stroke="var(--white)" stroke-width="1.6"/>
      </svg>
      info@brightmere.com
    </li>
    <li>
      <svg class="contact-icon" viewBox="0 0 26 26" aria-hidden="true">
        <circle cx="13" cy="13" r="13" fill="var(--orange)"/>
        <circle cx="13" cy="13" r="7" fill="none" stroke="var(--white)" stroke-width="1.6"/>
        <path d="M6 13h14M13 6c-3 4-3 10 0 14M13 6c3 4 3 10 0 14" fill="none" stroke="var(--white)" stroke-width="1.2"/>
      </svg>
      www.brightmere.com
    </li>
  </ul>

  <address class="mailing-address">42-10 Fenwick Ave 12<br>Larkdale, NY 11402</address>
</section>

<section class="card card-back">
  <div class="world-map" role="img" aria-label="Faint world map silhouette behind the name"></div>
  <div class="brand-lockup">
    <span class="brand-name">BRIGHTMERE</span>
    <span class="brand-tagline">Environmental Credit Company</span>
  </div>
</section>

</body>
</html>
```